" A Empresa busca atender seus clientes com qualidade e preservar a sensação de segurança de forma discreta e eficiente. Atuamos com a segurança eletrônica, na venda e locação de equipamentos e serviços de CFTV, Alarme, Interfonia, Controle de Acesso, Monitoramento e Eventos. Empresa com mais de 10 anos de mercado e tradição em segurança. "

```html
<!DOCTYPE html>
<html lang="pt-BR">
<head>
<meta charset="UTF-8">
<title>Orbe Segurança – Cartão de visita</title>
<link rel="stylesheet" href="https://fonts.googleapis.com/css2?family=Montserrat:wght@400;500;600&display=swap">
<style>
  :root{
    --bg:#e9e7e4;
    --card-white:#ffffff;
    --card-black:#0d0d0d;
    --orange:#f0731f;
    --ink:#2b2b2b;
    --light:#f2f2f2;
    --muted:#9a9a9a;
  }
  html,body{margin:0;padding:0;width:1200px;height:1200px;overflow:hidden;background:var(--bg);}
  body{font-family:"Montserrat",sans-serif;position:relative;}
  .card{
    position:absolute;left:150px;width:900px;height:500px;
    border-radius:6px;overflow:hidden;
    box-shadow:0 10px 30px rgba(0,0,0,.18);
  }
  .card--front{top:60px;background:var(--card-white);}
  .card--back{top:640px;background:var(--card-black);}

  .brand{
    position:absolute;left:0;right:0;top:0;bottom:0;
    display:flex;align-items:center;justify-content:center;gap:26px;
  }
  .brand__dot{width:84px;height:84px;border-radius:50%;background:var(--orange);}
  .brand__name{
    font-weight:500;font-size:58px;letter-spacing:3px;color:var(--ink);
  }

  .holder{position:absolute;left:70px;top:70px;color:var(--light);}
  .holder__name{font-weight:600;font-size:28px;letter-spacing:5px;margin:0;}
  .holder__role{font-weight:400;font-size:18px;letter-spacing:3px;color:var(--muted);margin:8px 0 0;}

  .contacts{position:absolute;left:70px;top:200px;list-style:none;margin:0;padding:0;}
  .contacts li{
    display:flex;align-items:flex-start;gap:22px;margin-bottom:30px;
    color:var(--light);font-size:15px;letter-spacing:2px;line-height:1.55;
  }
  .contacts svg{flex:none;width:26px;height:26px;margin-top:4px;}

  .decor{position:absolute;right:-150px;top:40px;width:560px;height:560px;border-radius:50%;background:var(--orange);}
</style>
</head>
<body>
  <section class="card card--front" aria-label="Frente do cartão">
    <div class="brand">
      <span class="brand__dot"></span>
      <span class="brand__name">ORBE SEGURANÇA</span>
    </div>
  </section>

  <section class="card card--back" aria-label="Verso do cartão">
    <div class="decor"></div>
    <div class="holder">
      <p class="holder__name">NOME SOBRENOME</p>
      <p class="holder__role">seu cargo</p>
    </div>
    <ul class="contacts">
      <li>
        <svg viewBox="0 0 24 24" fill="none" stroke="#f2f2f2" stroke-width="1.8"><path d="M12 22s7-7.2 7-12.5A7 7 0 0 0 5 9.5C5 14.8 12 22 12 22z"/><circle cx="12" cy="9.5" r="2.5"/></svg>
        <span>Endereço, nº 00<br>Cep: 00000-000</span>
      </li>
      <li>
        <svg viewBox="0 0 24 24" fill="none" stroke="#f2f2f2" stroke-width="1.8"><rect x="7" y="2" width="10" height="20" rx="2"/><line x1="11" y1="18.5" x2="13" y2="18.5"/></svg>
        <span>(00) 0000-0000<br>(00) 0000-0000</span>
      </li>
      <li>
        <svg viewBox="0 0 24 24" fill="none" stroke="#f2f2f2" stroke-width="1.8"><circle cx="12" cy="12" r="4"/><path d="M16 12v1.5a2.5 2.5 0 0 0 5 0V12a9 9 0 1 0-3.5 7.1"/></svg>
        <span>contato@orbeseg.com.br<br>www.orbeseg.com.br</span>
      </li>
    </ul>
  </section>
</body>
</html>
```